Home Page Website Design

The Site width is 1000 px. I've attached a Balsamiq mockup as a design layout guide. The design needs to be flat and clean. Please stick to the pixel dimensions of the mock up as the site will be responsive. I've also attached the logos used on the mockup for positional purposes.

Colours to use: Black, Grey, Green (Logo tie in) & green complementary colours.

Green (Logo tie in)
White Background
Titles: Black (Roboto Bold 700)
Text: Dark Grey (Roboto Normal 400)

Look & Style Example
http://www.brindlevox.org.uk/

Type Face
Google Fonts - Roboto

These are just guidelines, please feel free to use you own creative judgment.

Thanks

```html
<!DOCTYPE html>
<html lang="en">
<head>
<meta charset="utf-8">
<title>Wrekin Vale Teaching Alliance – Home</title>
<link href="https://fonts.googleapis.com/css2?family=Signika:wght@300;400;600&display=swap" rel="stylesheet">
<style>
:root{
  --green:#0a9e46;
  --green-dark:#078638;
  --green-light:#1fb556;
  --ink:#222;
  --text:#6b6b6b;
  --grey-band:#f1f1f1;
  --panel:#e3e3e3;
  --nav-top:#4a4a4a;
  --nav-bottom:#2a2a2a;
  --footer:#efefef;
  --bottom:#333;
  --white:#fff;
}
*{box-sizing:border-box;margin:0;padding:0}
html,body{width:972px;height:1200px;overflow:hidden;background:var(--white)}
body{font-family:"Signika",sans-serif;color:var(--text)}
.page{position:relative;width:972px;height:1200px;overflow:hidden}
.abs{position:absolute}

/* header */
.header-top{left:0;top:0;width:972px;height:51px;background:var(--white)}
.header-band{left:0;top:51px;width:972px;height:50px;background:var(--grey-band)}
.brand{left:65px;top:30px;display:flex;align-items:center;gap:8px;color:var(--green);font-size:17px;font-weight:600}
.brand-mark{width:14px;height:14px;background:var(--green)}
.util{top:18px;display:flex;align-items:center;gap:6px;font-size:12px;color:var(--ink)}
.util-divider{left:839px;top:14px;width:1px;height:24px;background:#ddd}
.register{left:581px;top:69px;font-size:15px;font-weight:600;color:var(--green)}
.email-box{left:686px;top:63px;width:221px;height:28px;border:1px solid #d6d6d6;background:#fff;font-size:11px;color:#999;padding:7px 15px}
.submit{left:856px;top:65px;width:49px;height:24px;background:linear-gradient(#9a9a9a,#777);color:#fff;font-size:11px;font-weight:600;text-align:center;line-height:24px}

/* nav */
.nav{left:0;top:101px;width:972px;height:43px;background:linear-gradient(var(--nav-top),var(--nav-bottom))}
.nav-list{left:65px;top:101px;height:43px;display:flex;list-style:none}
.nav-list li{height:43px;line-height:43px;padding:0 11px;font-size:12px;color:#fff;border-right:1px solid #1f1f1f;box-shadow:1px 0 0 #555}
.nav-list li.active{background:#222;color:#4ed07f;padding:0 13px}
.search{left:732px;top:109px;width:176px;height:27px;background:#fff;font-size:11px;color:#888;padding:6px 12px}

/* hero */
.hero-copy{left:64px;top:155px;width:333px;height:245px;background:linear-gradient(var(--green-light),var(--green-dark));color:#fff;padding:12px 15px}
.hero-copy h1{font-size:24px;font-weight:600;text-align:center;margin-bottom:10px}
.hero-copy p{font-size:11px;line-height:20.3px;text-align:justify;font-weight:300}
.more-btn{left:151px;top:344px;width:161px;height:36px;background:linear-gradient(#fff,#e7e7e7);border-radius:3px;display:flex;align-items:center;gap:9px;padding-left:13px;font-size:18px;font-weight:300;color:#444}
.hero-photo{left:403px;top:155px;width:505px;height:245px;background:linear-gradient(100deg,#a9b3ae 0%,#dfe3df 45%,#c7ad97 65%,#9aa5a2 100%)}
.hero-caption{left:427px;top:344px;font-size:23px;font-weight:600;color:#fff;text-shadow:0 0 3px #000,0 0 2px #000}
.hero-next{left:834px;top:260px;width:33px;height:33px;border-radius:50%;background:rgba(255,255,255,.85)}

/* sections */
.section-title{top:418px;font-size:20px;font-weight:600;color:var(--green)}
.panel{top:452px;background:var(--panel);padding:8px}
.welcome{left:66px;width:268px;height:427px;background:#f3f3f3;border:1px solid #e0e0e0}
.video{left:74px;top:460px;width:253px;height:137px;background:linear-gradient(90deg,#2f4a3a,#3d5545 55%,#c9b49e 75%,#4c5e52)}
.welcome-text{left:74px;top:612px;width:253px;font-size:11px;line-height:20.3px;text-align:justify}
.welcome-text p{margin-bottom:7px}

.training{left:352px;width:269px;height:427px}
.train-btn{left:361px;width:252px;height:35px;background:linear-gradient(#555,#2b2b2b);border-bottom:1px solid #1c1c1c;display:flex;align-items:center;gap:10px;padding-left:13px;font-size:13px;color:#fff}
.chev-box{width:17px;height:17px;background:#9a9a9a;display:flex;align-items:center;justify-content:center}
.news-title{left:361px;top:664px;font-size:20px;font-weight:600;color:#444}
.news-box{left:361px;top:692px;width:252px;height:180px;background:#fff;padding:14px 10px 0 8px}
.news-item{margin-bottom:12px}
.news-item h3{font-size:11px;font-weight:400;color:var(--green);display:flex;align-items:center;gap:6px;margin-bottom:3px}
.news-item p{font-size:10.5px;line-height:17px;padding-left:12px;text-align:justify}

.courses{left:641px;width:267px;height:427px;background:#ddd}
.course{left:648px;width:252px;height:129px;background:#fff;padding:10px 13px}
.course h3{font-size:12px;font-weight:400;color:var(--green);line-height:18.5px;margin-bottom:7px}
.course p{font-size:10.5px;line-height:17px;margin-bottom:9px}
.course .meta{display:flex;justify-content:space-between;align-items:center;font-size:11px;color:var(--ink)}
.book{display:flex;align-items:center;gap:5px;font-size:15px;font-weight:300}
.toggle{left:893px;top:423px;width:14px;height:14px;border-radius:50%;border:1px solid #bbb;background:#fff}

/* footer */
.footer{left:0;top:898px;width:972px;height:257px;background:var(--footer)}
.footer-photo{left:67px;top:913px;width:104px;height:83px;border:3px solid #fff;background:linear-gradient(#7a96b5,#8e7f6a 55%,#6e7c58);box-shadow:0 0 0 1px #ddd}
.address{left:177px;top:913px;font-size:11px;line-height:20.3px;color:#666}
.address .hl{color:var(--green)}
.email-line{left:71px;top:1003px;font-size:11px;color:#666}
.email-line .hl{color:var(--green)}
.flinks{top:914px;list-style:none;font-size:11px;line-height:20.3px;color:#666}
.flinks li::before{content:"» ";color:#999}
.hub{left:662px;top:917px;display:flex;align-items:center;gap:8px;font-size:15px;color:#333;line-height:17px;width:110px}
.hub-mark{width:12px;height:12px;background:var(--green);flex:none}
.social{left:778px;width:127px;height:19px;font-size:9.5px;color:#fff;font-weight:600;display:flex;align-items:center;gap:8px;padding-left:8px;border-radius:2px}
.social.one{top:929px;background:linear-gradient(#4f6aa6,#3b5594)}
.social.two{top:963px;background:linear-gradient(#7fd0f2,#4db6e6)}
.social i{width:10px;height:10px;background:rgba(255,255,255,.85);display:block}
.footer-rule{left:64px;top:1039px;width:844px;height:1px;background:#d0d0d0}
.partners-title{left:0;top:1053px;width:972px;text-align:center;font-size:11px;color:#666}
.badge{position:absolute}
.bottom{left:0;top:1155px;width:972px;height:45px;background:var(--bottom);color:#ccc;font-size:11px;text-align:center;line-height:45px}
</style>
</head>
<body>
<div class="page">

  <!-- header -->
  <div class="abs header-top"></div>
  <div class="abs header-band"></div>
  <div class="abs brand"><span class="brand-mark"></span>Wrekin Vale Teaching Alliance</div>

  <div class="abs util" style="left:747px">
    <svg width="17" height="14" viewBox="0 0 17 14"><ellipse cx="6" cy="5" rx="6" ry="4.5" fill="#222"/><path d="M2 8l-1 4 4-2z" fill="#222"/><ellipse cx="11.5" cy="8.5" rx="5" ry="3.8" fill="#444"/></svg>
    LIVE CHAT
  </div>
  <div class="abs util-divider"></div>
  <div class="abs util" style="left:856px">
    <svg width="10" height="12" viewBox="0 0 10 12"><path d="M2.5 5V3.5a2.5 2.5 0 015 0V5" stroke="#222" stroke-width="1.5" fill="none"/><rect x="0.5" y="5" width="9" height="7" fill="#222"/></svg>
    LOG IN
  </div>

  <div class="abs register">REGISTER NOW</div>
  <div class="abs email-box">Email Address</div>
  <div class="abs submit">SUBMIT</div>

  <!-- navigation -->
  <div class="abs nav"></div>
  <ul class="abs nav-list">
    <li class="active">Home</li>
    <li>About us</li>
    <li>Training &amp; Developments</li>
    <li>Benefits</li>
    <li>Members</li>
    <li>What's On</li>
    <li>Contact us</li>
    <li>News</li>
    <li style="border-right:none;box-shadow:none">Forum</li>
  </ul>
  <div class="abs search">Search</div>
  <svg class="abs" style="left:880px;top:112px" width="20" height="20" viewBox="0 0 20 20"><circle cx="8" cy="8" r="6" stroke="#222" stroke-width="2.5" fill="none"/><path d="M12.5 12.5l6 6" stroke="#222" stroke-width="3.5" stroke-linecap="round"/></svg>

  <!-- hero -->
  <div class="abs hero-copy">
    <h1>New Teachers in Workshop</h1>
    <p>Donec sagittis urna id magna fringilla porta. Curabitur sem augue, rhoncus eu nisi sit amet, fermentum molestie diam. Fusce malesuada tempus metus, a molestie mi fringilla in. Cras sed nisi volutpat, dictum sem et, vulputate neque. Pellen tesque aliquam vel ligula vel malesuada. Duis ac risus sit amet enim vehicula hendrerit sed suscipit turpis.</p>
  </div>
  <div class="abs more-btn">
    <svg width="19" height="19" viewBox="0 0 19 19"><circle cx="9.5" cy="9.5" r="9.5" fill="#555"/><path d="M8 5.5l4 4-4 4" stroke="#fff" stroke-width="2" fill="none"/></svg>
    Find Out More
  </div>
  <div class="abs hero-photo" role="img" aria-label="Photo of a smiling student holding books in a bright school corridor"></div>
  <div class="abs hero-next"></div>
  <svg class="abs" style="left:845px;top:268px" width="12" height="17" viewBox="0 0 12 17"><path d="M3 2l6 6.5L3 15" stroke="#999" stroke-width="1.5" fill="none"/></svg>
  <div class="abs hero-caption">Suspendisse id metus turpis</div>

  <!-- welcome -->
  <div class="abs section-title" style="left:66px">Welcome to WVTA</div>
  <div class="abs welcome" style="top:452px"></div>
  <div class="abs video" role="img" aria-label="Video still of a teacher pointing at a chalkboard"></div>
  <svg class="abs" style="left:175px;top:502px" width="52" height="52" viewBox="0 0 52 52"><circle cx="26" cy="26" r="23" stroke="#fff" stroke-width="4" fill="rgba(0,0,0,.35)"/><path d="M20 15l18 11-18 11z" fill="#fff"/></svg>
  <div class="abs welcome-text">
    <p>Curabitur feugiat tortor in fringilla iaculis. Aenean sollicitudin pellentesque eros, sit amet rutrum tortor euismod vel. Sed tincidunt egestas risus, suscipit faucibus eros elementum in. Mauris a aliquam libero, ut tempus lectus. Donec semper tincidunt risus id dignissim.</p>
    <p>Donec sagittis urna id magna fringilla porta. Curabitur sem augue, rhoncus eu nisi sit amet, fermentum molestie diam. Fusce malesuada tempus metus, a molestie mi fringilla in. Cras sed nisi volutpat, dictum sem et, vulputate neque. Pellentesque aliquam vel ligula vel malesuada.</p>
  </div>

  <!-- training -->
  <div class="abs section-title" style="left:352px">Training &amp; Development</div>
  <div class="abs panel training"></div>
  <div class="abs train-btn" style="top:461px"><span class="chev-box"><svg width="8" height="10" viewBox="0 0 8 10"><path d="M2 1l4 4-4 4" stroke="#fff" stroke-width="1.6" fill="none"/></svg></span>LEADERSHIP TRAINING</div>
  <div class="abs train-btn" style="top:497px"><span class="chev-box"><svg width="8" height="10" viewBox="0 0 8 10"><path d="M2 1l4 4-4 4" stroke="#fff" stroke-width="1.6" fill="none"/></svg></span>CPD</div>
  <div class="abs train-btn" style="top:533px"><span class="chev-box"><svg width="8" height="10" viewBox="0 0 8 10"><path d="M2 1l4 4-4 4" stroke="#fff" stroke-width="1.6" fill="none"/></svg></span>SCHOOL 2 SCHOOL SUPPORT</div>
  <div class="abs train-btn" style="top:570px"><span class="chev-box"><svg width="8" height="10" viewBox="0 0 8 10"><path d="M2 1l4 4-4 4" stroke="#fff" stroke-width="1.6" fill="none"/></svg></span>RESEARCH &amp; DEVELOPMENT</div>
  <div class="abs train-btn" style="top:606px"><span class="chev-box"><svg width="8" height="10" viewBox="0 0 8 10"><path d="M2 1l4 4-4 4" stroke="#fff" stroke-width="1.6" fill="none"/></svg></span>ITI (SCHOOL DIRECT)</div>

  <div class="abs news-title">News</div>
  <div class="abs news-box">
    <div class="news-item">
      <h3><svg width="6" height="9" viewBox="0 0 6 9"><path d="M1 1l3.5 3.5L1 8" stroke="#0a9e46" stroke-width="1.8" fill="none"/></svg>Nulla eu gravida erat</h3>
      <p>Curabitur sem augue, rhoncus eu nisi sit amet, fermentum molestie diam. Fusce malesuada tempus metus, a molestie mi.</p>
    </div>
    <div class="news-item">
      <h3><svg width="6" height="9" viewBox="0 0 6 9"><path d="M1 1l3.5 3.5L1 8" stroke="#0a9e46" stroke-width="1.8" fill="none"/></svg>Nulla eu gravida erat</h3>
      <p>Curabitur sem augue, rhoncus eu nisi sit amet, fermentum molestie diam. Fusce malesuada tempus metus, a molestie mi.</p>
    </div>
  </div>

  <!-- courses -->
  <div class="abs section-title" style="left:641px">Latest Courses</div>
  <div class="abs toggle"></div>
  <svg class="abs" style="left:898px;top:428px" width="5" height="4" viewBox="0 0 5 4"><path d="M0 0h5L2.5 4z" fill="#555"/></svg>
  <div class="abs panel courses"></div>

  <div class="abs course" style="top:460px">
    <h3>Want to deliver consistently “Outstanding” Lessons?</h3>
    <p>Curabitur sem augue, rhoncus eu nisi sit amet, fermentum molestie diam.</p>
    <div class="meta"><span>6 Places Left</span><span class="book"><svg width="12" height="13" viewBox="0 0 12 13"><rect x="0.5" y="0.5" width="11" height="12" fill="#333"/><path d="M3 4h6M3 6.5h6M3 9h6" stroke="#fff" stroke-width="1"/></svg>BOOK</span></div>
  </div>
  <div class="abs course" style="top:602px">
    <h3>Want to deliver consistently “Outstanding” Lessons?</h3>
    <p>Curabitur sem augue, rhoncus eu nisi sit amet, fermentum molestie diam.</p>
    <div class="meta"><span>6 Places Left</span></div>
  </div>
  <div class="abs course" style="top:742px">
    <h3>Want to deliver consistently “Outstanding” Lessons?</h3>
    <p>Curabitur sem augue, rhoncus eu nisi sit amet, fermentum molestie diam.</p>
    <div class="meta"><span>6 Places Left</span><span class="book"><svg width="12" height="13" viewBox="0 0 12 13"><rect x="0.5" y="0.5" width="11" height="12" fill="#333"/><path d="M3 4h6M3 6.5h6M3 9h6" stroke="#fff" stroke-width="1"/></svg>BOOK</span></div>
  </div>

  <!-- footer -->
  <div class="abs footer"></div>
  <div class="abs footer-photo" role="img" aria-label="Photo of the alliance's school building"></div>
  <div class="abs address">
    Wrekin Vale Teaching Alliance<br>
    Mill Bank Road<br>
    Ashbury<br>
    Tel : <span class="hl">01632 960400</span>
  </div>
  <div class="abs email-line">Email : <span class="hl">info@wrekinvaleteaching.co.uk</span></div>

  <ul class="abs flinks" style="left:361px">
    <li>About us</li><li>Training &amp; Development</li><li>Benefits</li><li>Members</li><li>Calendar of Events</li>
  </ul>
  <ul class="abs flinks" style="left:547px">
    <li>Contact us</li><li>News</li><li>Forums</li><li>Sitemap</li>
  </ul>

  <div class="abs hub"><span class="hub-mark"></span>Regional Teaching Hub</div>

  <div class="abs social one"><i></i>Sign in with Linkspace</div>
  <div class="abs social two"><i></i>Sign in with Chirper</div>

  <div class="abs footer-rule"></div>
  <div class="abs partners-title">Partners Schools</div>

  <div class="badge" style="left:70px;top:1085px;width:34px;height:36px;background:#c9ccd6;border-radius:3px 3px 14px 14px"></div>
  <div class="badge" style="left:131px;top:1082px;width:28px;height:36px;background:#5a8f5a;border-radius:2px 2px 14px 14px"></div>
  <div class="badge" style="left:180px;top:1084px;width:32px;height:32px;background:#a9b36a;border-radius:50%"></div>
  <div class="badge" style="left:233px;top:1090px;width:36px;height:38px;background:#1b2f9a"></div>
  <div class="badge" style="left:291px;top:1094px;width:30px;height:30px;background:#6a79b8;border-radius:50%"></div>
  <div class="badge" style="left:345px;top:1094px;width:32px;height:30px;background:#5d6fa8;border-radius:4px"></div>
  <div class="badge" style="left:399px;top:1098px;width:64px;height:26px;background:#3c5a8a"></div>
  <div class="badge" style="left:487px;top:1100px;width:52px;height:20px;background:#d9c98a;border-radius:3px"></div>
  <div class="badge" style="left:565px;top:1083px;width:28px;height:58px;background:#a46a78;border-radius:3px 3px 14px 14px"></div>
  <div class="badge" style="left:610px;top:1099px;width:73px;height:25px;background:#2f8fca"></div>
  <div class="badge" style="left:702px;top:1100px;width:24px;height:24px;background:#d42a3a;border-radius:50%"></div>
  <div class="badge" style="left:730px;top:1105px;width:40px;height:14px;background:#c8c8c8"></div>
  <div class="badge" style="left:793px;top:1095px;width:32px;height:32px;background:#2c3f7a;border-radius:2px 2px 14px 14px"></div>
  <div class="badge" style="left:843px;top:1095px;width:60px;height:28px;background:#c4cddc;border-radius:3px"></div>

  <div class="abs bottom">Copyright © 2013 &nbsp;Wrekin Vale Teaching Alliance.</div>
</div>
</body>
</html>
```